依頼概要
■依頼の目的/概要
小学生バレーボールのスポーツ少年団でメンバーを募集するためのポスターの作成をお願いします。

■依頼詳細
ポスターは男子チーム、女子チーム兼用となります。主に教室での直接配布、校内の掲示板や近隣の施設(コンビニや公民館等)での掲示を目的としたものになります。

必要に応じて写真の背景等を加工いただいても構いません。

楽しそうなイメージだけでなく、スポーツに関心のある子どもたちがバレーボールを“かっこいい”と感じてくれるような躍動感の伝わるものを希望しています。

■重視する点
・明るくインパクトのあるデザイン
・できるだけ躍動感の伝わるもの
・読みやすい文字であること

■サイズ
A4サイズでお願いします。
メインはA4ですが、B4(A4の122%)にも対応する画素数でお願いいたします

■その他
・レイアウトイメージ、素材は添付ファイルにてご確認ください
・写真やイラストの素材は当方で用意していますが、用意したもの以外の素材を使っていただいても構いません。
・レイアウトのイメージやキャッチコピー、掲載する文言等は添付の「レイアウトイメージ.pdf」「レイアウト説明.txt」を参照ください。レイアウトは当方のイメージと異なるものになっても構いません。

何かご不明な点がございましたら、お気軽にご質問下さい。
どうぞよろしくお願いいたします。
納品いただくデータですが、納品後に当方で編集することがあるため、フォトショップまたはイラストレーターで編集できるかたちで納品いただけますと幸いです。よろしくお願いします。

```html
<!DOCTYPE html>
<html lang="ja">
<head>
<meta charset="utf-8">
<title>青空バレースポーツ少年団 メンバー募集</title>
<link href="https://fonts.googleapis.com/css2?family=Dela+Gothic+One&family=M+PLUS+Rounded+1c:wght@500;800;900&display=swap" rel="stylesheet">
<style>
:root{
  --yellow:#ffd400;
  --yellow-deep:#ffb400;
  --ink:#111111;
  --navy:#1d2a6b;
  --red:#e60f1e;
  --pink:#ff4f8b;
  --blue:#2f8fe0;
  --white:#ffffff;
}
*{margin:0;padding:0;box-sizing:border-box}
html,body{width:849px;height:1200px;overflow:hidden;background:var(--white)}
.poster{position:relative;width:849px;height:1200px;overflow:hidden;
  background:radial-gradient(circle at 45% 42%,#fff6b0 0,var(--yellow) 38%,var(--yellow-deep) 100%);
  font-family:"M PLUS Rounded 1c",sans-serif;color:var(--ink)}
.photo{position:absolute;border:5px solid var(--white);box-shadow:0 3px 8px rgba(0,0,0,.35);
  background:linear-gradient(160deg,#c9c4bd,#8b8f96 60%,#6e5b55)}
.photo--a{left:14px;top:10px;width:230px;height:160px;transform:rotate(-3deg)}
.photo--b{left:236px;top:8px;width:200px;height:145px;transform:rotate(4deg)}
.photo--c{left:40px;top:170px;width:190px;height:130px;transform:rotate(2deg)}
.photo--d{left:175px;top:230px;width:145px;height:95px;transform:rotate(-5deg)}
.illust{position:absolute;border-radius:40% 45% 35% 40%}
.illust--spiker{left:530px;top:0;width:310px;height:320px;background:linear-gradient(180deg,#ffe2c4,#e8412f 55%,#283a8f)}
.illust--ball{left:335px;top:165px;width:140px;height:140px;border-radius:50%;background:radial-gradient(circle at 35% 35%,#fff,#dfe4ec 60%,#9aa7bd)}
.illust--receiver{left:10px;top:700px;width:220px;height:195px;background:linear-gradient(180deg,#ffe2c4,#e8412f 50%,#283a8f)}
.illust--cheer{left:690px;top:880px;width:140px;height:120px;background:linear-gradient(180deg,#ffe2c4,#e8412f 55%,#283a8f)}
.bubble{position:absolute;background:var(--white);border:3px solid var(--ink);border-radius:50%;
  display:flex;align-items:center;justify-content:center;text-align:center;font-weight:800;line-height:1.25}
.bubble--motto{left:470px;top:20px;width:190px;height:92px;font-size:17px;color:var(--red)}
.bubble--cheer{left:8px;top:232px;width:118px;height:100px;font-size:14px;color:var(--red);transform:rotate(-6deg)}
.title{position:absolute;left:0;top:335px;width:849px;height:300px;transform:rotate(-3deg);
  font-family:"Dela Gothic One",sans-serif;font-weight:400;color:var(--ink);line-height:1;white-space:nowrap;
  -webkit-text-stroke:12px var(--white);paint-order:stroke fill}
.title__line{position:absolute;display:block}
.title__line--1{left:22px;top:0;font-size:96px}
.title__line--2{left:20px;top:100px;font-size:126px;letter-spacing:-6px}
.title__line--3{right:20px;top:225px;font-size:86px}
.tag{position:absolute;left:180px;top:618px;width:140px;height:72px;border-radius:50%;
  background:var(--blue);color:var(--white);font-size:13px;font-weight:800;
  display:flex;align-items:center;justify-content:center;text-align:center;line-height:1.25;transform:rotate(-10deg)}
.team{position:absolute;left:240px;top:690px;width:500px;text-align:center;white-space:nowrap;
  font-size:34px;font-weight:900;color:var(--white);
  -webkit-text-stroke:7px var(--navy);paint-order:stroke fill}
.recruit{position:absolute;left:240px;top:738px;width:495px;height:62px;background:var(--white);
  border:4px solid var(--ink);display:flex;align-items:center;justify-content:center;white-space:nowrap;
  font-size:44px;font-weight:900;color:var(--red);letter-spacing:-1px}
.badge{position:absolute;left:748px;top:690px;width:92px;height:92px;border-radius:50%;
  background:var(--pink);color:var(--white);font-size:13px;font-weight:800;
  display:flex;align-items:center;justify-content:center;text-align:center;line-height:1.3}
.message{position:absolute;left:250px;top:810px;width:480px;font-size:16px;font-weight:800;line-height:1.6}
.schedule{position:absolute;left:14px;top:905px;width:665px;background:var(--white);border:3px solid var(--ink);
  border-radius:10px;padding:8px 12px;display:flex;gap:12px;align-items:center}
.schedule__label{font-size:19px;font-weight:900;line-height:1.3;text-align:center;white-space:nowrap}
.schedule__rows{font-size:14px;font-weight:800;line-height:1.8;white-space:nowrap}
.schedule__day{display:inline-block;width:82px;color:var(--red)}
.schedule__time{color:var(--red);margin-left:8px}
.cta{position:absolute;left:0;top:1012px;width:849px;height:56px;background:var(--navy);
  color:var(--yellow);font-size:32px;font-weight:900;display:flex;align-items:center;padding-left:20px;letter-spacing:-1px}
.footer{position:absolute;left:0;top:1068px;width:849px;height:132px;background:var(--white);
  display:flex;justify-content:space-between;align-items:center;padding:0 20px}
.footer__notes{font-size:14px;font-weight:800;line-height:1.8}
.contact{text-align:right;font-weight:900}
.contact__org{font-size:18px}
.contact__phone{display:flex;align-items:center;gap:6px;justify-content:flex-end;font-size:18px}
.contact__number{font-size:40px;color:var(--red);letter-spacing:-1px}
.contact__icon{width:30px;height:30px}
</style>
</head>
<body>
<main class="poster">
  <div class="photo photo--a" role="img" aria-label="体育館でレシーブ練習をする子どもたちの写真"></div>
  <div class="photo photo--b" role="img" aria-label="チームで練習する子どもたちの写真"></div>
  <div class="photo photo--c" role="img" aria-label="スパイクを打つ子どもの写真"></div>
  <div class="photo photo--d" role="img" aria-label="試合中の子どもたちの写真"></div>
  <div class="illust illust--spiker" role="img" aria-label="スパイクを打つ少年のイラスト"></div>
  <div class="illust illust--ball" role="img" aria-label="勢いよく飛ぶバレーボールのイラスト"></div>

  <div class="bubble bubble--motto">チョウのように舞い！<br>ハチのように刺す！</div>
  <div class="bubble bubble--cheer">レシーブ！<br>スパイク！<br>キマると<br>気持ちいい！</div>

  <h1 class="title">
    <span class="title__line title__line--1">そうだ、</span>
    <span class="title__line title__line--2">バレーボール</span>
    <span class="title__line title__line--3">しよう。</span>
  </h1>

  <div class="tag">初心者だって大歓迎！<br>身長が低くても<br>大丈夫！</div>
  <div class="illust illust--receiver" role="img" aria-label="レシーブする少女のイラスト"></div>

  <p class="team">青空バレースポーツ少年団</p>
  <p class="recruit">男女新メンバー募集!!</p>
  <div class="badge">保護者の<br>方も歓迎<br>しています！</div>

  <p class="message">みんなで下の名前でよびあう青空バレーは仲のよさが自慢！<br>いろいろな小学校から集まっているから<br>友だちもたくさんできるよ！</p>

  <section class="schedule">
    <div class="schedule__label">練習日<br>(毎週)</div>
    <div class="schedule__rows">
      <div><span class="schedule__day">土・日曜日</span>青空小学校体育館・青空北小学校体育館<span class="schedule__time">9:00〜</span></div>
      <div><span class="schedule__day">水曜日</span>青空小学校体育館<span class="schedule__time">17:30〜</span></div>
    </div>
  </section>
  <div class="illust illust--cheer" role="img" aria-label="応援する子どものイラスト"></div>

  <p class="cta">見学・体験はいつでも受け付けています!</p>

  <footer class="footer">
    <div class="footer__notes">連絡は右記の担当 山田までどうぞ。<br>持ち物：上ぐつ、水とう、動きやすい服そう</div>
    <div class="contact">
      <div class="contact__org">連絡先/青空バレースポーツ少年団</div>
      <div class="contact__phone">育成会会長 山田
        <svg class="contact__icon" viewBox="0 0 24 24"><path fill="#e60f1e" d="M6.6 10.8a15.1 15.1 0 0 0 6.6 6.6l2.2-2.2c.3-.3.7-.4 1-.2 1.1.4 2.3.6 3.6.6.6 0 1 .4 1 1V20c0 .6-.4 1-1 1A17 17 0 0 1 3 4c0-.6.4-1 1-1h3.5c.6 0 1 .4 1 1 0 1.3.2 2.5.6 3.6.1.3 0 .7-.2 1z"/></svg>
        <span class="contact__number">090-1234-5678</span>
      </div>
    </div>
  </footer>
</main>
</body>
</html>
```